Design a visually appealing layout for our company mission and values. I want to create a visually appealing 1 page flyer that presents our company mission and values to clients as well as to our internal team/staff. We will utilize the 1 page flyer in internal and external presentations about our company. We will also use the flyer in sales proposals/marketing packages.

Target Market(s)

Internal team members as well as external prospective clients, existing clients & referral partners

Industry/Entity Type

Financial Service

Colors

Designer to choose colors to be used in the design.

Requirements
Must have
• Should reflect our company brand so I have included our Pantone panel, fonts etc. I have provided our company logo as well which should be part of the branded document
Nice to have
• I would like the presentation to be useable in different formats and to different audiences so something that is more graphic/visual heavy - otherwise it's a lot of words that people don't read.
• Would like to be able to easily include in our corporate template powerpoint presentation.

```html
<!DOCTYPE html>
<html lang="en">
<head>
<meta charset="utf-8">
<title>Our Mission – Northvale Retirement Partners</title>
<link href="https://fonts.googleapis.com/css2?family=Montserrat:wght@500;600;700;800&family=Open+Sans:wght@400;600&display=swap" rel="stylesheet">
<style>
  :root {
    --bg: #3a3a3a;
    --paper: #ffffff;
    --blue: #1f6fb2;
    --navy: #163f6e;
    --green: #8cc63f;
    --green-soft: #b9dc8e;
    --ink: #222a33;
    --photo-a: #eceef0;
    --photo-b: #c9ced4;
  }
  * { box-sizing: border-box; margin: 0; padding: 0; }
  html, body { width: 1200px; height: 900px; overflow: hidden; background: var(--bg); }
  .flyer {
    position: absolute; left: 268px; top: 18px;
    width: 664px; height: 864px;
    background: var(--paper); overflow: hidden;
    font-family: "Open Sans", Arial, sans-serif; color: var(--ink);
  }
  .hero {
    position: absolute; left: 0; top: 0; width: 100%; height: 318px;
    background: linear-gradient(100deg, var(--photo-a) 0%, #f6f7f8 60%, #ffffff 100%);
  }
  .hero-photo {
    position: absolute; left: 30px; top: 14px; width: 300px; height: 304px;
    background: linear-gradient(90deg, #3d5c94 0%, #5a72a0 45%, #e4e7ea 75%, var(--photo-a) 100%);
    opacity: .8;
  }
  .brand { position: absolute; right: 36px; top: 28px; text-align: left; }
  .brand-name {
    display: flex; align-items: center; gap: 10px;
    font-family: "Montserrat", sans-serif; font-weight: 600;
    color: var(--navy); font-size: 17px; line-height: 1.15; letter-spacing: .5px;
    text-transform: uppercase;
  }
  .brand-dot { width: 34px; height: 34px; border-radius: 50%; background: var(--blue); flex: none; }
  .tagline {
    margin-top: 10px; font-family: "Montserrat", sans-serif; font-weight: 500;
    font-size: 9.5px; letter-spacing: 2px; color: var(--ink); text-transform: uppercase;
  }
  .mission {
    position: absolute; right: 0; top: 168px; width: 342px; height: 150px;
    background: var(--blue); border-top-left-radius: 34px;
    color: #fff; text-align: right; padding: 26px 30px 0 20px;
    font-family: "Montserrat", sans-serif;
  }
  .mission h1 { font-weight: 800; font-size: 31px; letter-spacing: .5px; line-height: 1; }
  .mission p { font-weight: 600; font-size: 15.5px; line-height: 1.2; margin-top: 6px; text-transform: uppercase; }
  .values { position: absolute; left: 0; top: 318px; width: 100%; height: 494px; }
  .timeline { position: absolute; left: 132px; top: 22px; width: 3px; height: 458px; background: var(--navy); }
  .value { position: absolute; left: 0; width: 100%; height: 64px; }
  .value-icon { position: absolute; left: 70px; top: 0; width: 54px; height: 54px; }
  .value-notch {
    position: absolute; left: 134px; top: 14px; width: 0; height: 0;
    border-top: 6px solid transparent; border-bottom: 6px solid transparent;
    border-left: 7px solid var(--navy);
  }
  .value-text { position: absolute; left: 150px; top: 0; right: 64px; }
  .value-text h2 {
    font-family: "Montserrat", sans-serif; font-weight: 700; font-size: 13px;
    color: var(--navy); text-transform: uppercase; letter-spacing: .3px;
  }
  .value-text p { font-size: 12.5px; line-height: 1.3; margin-top: 2px; }
  .footer-line { position: absolute; left: 0; bottom: 46px; width: 100%; height: 6px; background: var(--green); }
  .footer-band { position: absolute; left: 0; bottom: 0; width: 100%; height: 46px; background: var(--blue); }
</style>
</head>
<body>
<main class="flyer">
  <section class="hero">
    <div class="hero-photo" role="img" aria-label="Photo of a smiling mature couple standing together"></div>
    <div class="brand">
      <div class="brand-name"><span class="brand-dot"></span><span>Northvale<br>Retirement Partners</span></div>
      <div class="tagline">Plan ahead. Retire with confidence.</div>
    </div>
    <div class="mission">
      <h1>OUR MISSION</h1>
      <p>To proactively<br>support organizations<br>and lead them toward<br>a secure future</p>
    </div>
  </section>

  <section class="values">
    <div class="timeline"></div>

    <article class="value" style="top:22px">
      <svg class="value-icon" viewBox="0 0 52 52"><circle cx="26" cy="26" r="24" fill="var(--green-soft)" stroke="var(--navy)" stroke-width="2"/><g fill="none" stroke="var(--navy)" stroke-width="1.8"><circle cx="26" cy="26" r="5"/><circle cx="15" cy="17" r="3.5"/><circle cx="37" cy="17" r="3.5"/><circle cx="15" cy="35" r="3.5"/><circle cx="37" cy="35" r="3.5"/><path d="M18 19l4 4M34 19l-4 4M18 33l4-4M34 33l-4-4"/></g></svg>
      <span class="value-notch"></span>
      <div class="value-text"><h2>Teamwork:</h2><p>Collaborating with team members, clients and partners to maintain a high level of communication, accountability and engagement to achieve our common goals</p></div>
    </article>

    <article class="value" style="top:89px">
      <svg class="value-icon" viewBox="0 0 52 52"><circle cx="26" cy="26" r="24" fill="var(--green-soft)" stroke="var(--navy)" stroke-width="2"/><g fill="none" stroke="var(--navy)" stroke-width="1.8"><circle cx="18" cy="17" r="4"/><path d="M12 38v-9a6 6 0 0 1 12 0v9"/><rect x="28" y="30" width="4" height="8"/><rect x="34" y="25" width="4" height="13"/><circle cx="34" cy="15" r="5"/></g><text x="34" y="18" font-size="7" text-anchor="middle" fill="var(--navy)" font-family="Montserrat, sans-serif" font-weight="700">$</text></svg>
      <span class="value-notch"></span>
      <div class="value-text"><h2>Financial Empowerment:</h2><p>We commit ourselves to providing the best retirement solutions to guide our clients toward financial freedom</p></div>
    </article>

    <article class="value" style="top:156px">
      <svg class="value-icon" viewBox="0 0 52 52"><circle cx="26" cy="26" r="24" fill="var(--green-soft)" stroke="var(--navy)" stroke-width="2"/><g fill="none" stroke="var(--navy)" stroke-width="1.8"><circle cx="26" cy="22" r="7"/><circle cx="26" cy="22" r="2.5"/><path d="M26 12v3M26 29v3M16 22h3M33 22h3"/><path d="M12 32c4 0 7 4 14 4s10-4 14-4"/></g></svg>
      <span class="value-notch"></span>
      <div class="value-text"><h2>Knowledge:</h2><p>Our team of highly trained and credentialed experts work to educate and lead our clients toward success</p></div>
    </article>

    <article class="value" style="top:223px">
      <svg class="value-icon" viewBox="0 0 52 52"><circle cx="26" cy="26" r="24" fill="var(--green-soft)" stroke="var(--navy)" stroke-width="2"/><g fill="none" stroke="var(--navy)" stroke-width="1.8"><path d="M14 36l8-8 5 5 11-13"/><path d="M33 20h5v5"/><path d="M14 16h10M14 21h6"/></g></svg>
      <span class="value-notch"></span>
      <div class="value-text"><h2>Proactivity:</h2><p>We hold ourselves accountable in anticipating regulatory changes and keeping you and your plan in compliance</p></div>
    </article>

    <article class="value" style="top:290px">
      <svg class="value-icon" viewBox="0 0 52 52"><circle cx="26" cy="26" r="24" fill="var(--green-soft)" stroke="var(--navy)" stroke-width="2"/><g fill="none" stroke="var(--navy)" stroke-width="1.8"><path d="M17 27a6 6 0 0 1 2-11 8 8 0 0 1 15 2 5 5 0 0 1 1 9z"/><rect x="20" y="28" width="12" height="10" rx="1.5"/><path d="M23 32h6M23 35h4"/></g></svg>
      <span class="value-notch"></span>
      <div class="value-text"><h2>Dedication:</h2><p>We provide exceptional customer service and ensure that we are friendly, timely and responsive whenever corresponding with our clients</p></div>
    </article>

    <article class="value" style="top:357px">
      <svg class="value-icon" viewBox="0 0 52 52"><circle cx="26" cy="26" r="24" fill="var(--green-soft)" stroke="var(--navy)" stroke-width="2"/><g fill="none" stroke="var(--navy)" stroke-width="2"><path d="M26 12l11 4v8c0 8-5 13-11 16-6-3-11-8-11-16v-8z"/><path d="M21 26l4 4 7-8"/></g></svg>
      <span class="value-notch"></span>
      <div class="value-text"><h2>Security:</h2><p>With an emphasis on high technological standards, we lead you toward peace of mind that your savings and investments are protected</p></div>
    </article>

    <article class="value" style="top:424px">
      <svg class="value-icon" viewBox="0 0 52 52"><circle cx="26" cy="26" r="24" fill="var(--green-soft)" stroke="var(--navy)" stroke-width="2"/><g fill="none" stroke="var(--navy)" stroke-width="2"><circle cx="23" cy="23" r="8"/><path d="M29 29l8 8"/><circle cx="23" cy="23" r="2.5"/></g></svg>
      <span class="value-notch"></span>
      <div class="value-text"><h2>Transparency:</h2><p>We take pride in representing the retirement plan industry as an open, honest, and socially responsible firm with our clients</p></div>
    </article>
  </section>

  <div class="footer-line"></div>
  <div class="footer-band"></div>
</main>
</body>
</html>
```